High end landscaping & service company needs brochure design

Please check out our website.

We would like the brochure to be about our landscape Construction (Outdoor Kitchens, water features, gardens), Turf Care (Fertilizer, aeration, over seeding), property maintenance (Lawn maintenance, Gardens)

I would like our brochure to have a similar theme and look as our current post card and website. Our website is www.brinvalelandworks.com

Please let me know if you need any further information. dorrel@brinvalelandworks.com

Thanks,

Target Market(s)

High End commercial and residential clients

Industry/Entity Type

Property Maintenance

Requirements
Must have
• BRIEF price list for Turf Care

Use contact info on website.

1 double sided page so we can print it and mail it OR send it as a email.

```html
<!DOCTYPE html>
<html lang="en">
<head>
<meta charset="utf-8">
<title>Brinvale Landworks Group – Brochure</title>
<link href="https://fonts.googleapis.com/css2?family=Oswald:wght@500;600&family=Open+Sans:wght@400;600;700&display=swap" rel="stylesheet">
<style>
:root{
  --green:#3d8b2f;
  --green-dark:#2b6a22;
  --wood:#4b2f1d;
  --wood-light:#6b4429;
  --cream:#f6f3ea;
  --rule:#d9d3c2;
  --ink:#3c3c3c;
  --white:#ffffff;
}
*{margin:0;padding:0;box-sizing:border-box}
html,body{width:878px;height:1200px;overflow:hidden;background:var(--white)}
.brochure{position:relative;width:878px;height:1200px;overflow:hidden;
  background:linear-gradient(90deg,var(--wood) 0%,var(--wood-light) 35%,var(--wood) 60%,var(--wood-light) 85%,var(--wood) 100%);
  font-family:"Open Sans",Arial,sans-serif;color:var(--ink)}
.masthead{position:absolute;left:0;top:0;width:878px;height:145px;background:var(--white);
  display:flex;align-items:center;justify-content:center;gap:16px}
.brand-dot{width:62px;height:62px;border-radius:50%;background:var(--green)}
.brand-name{font-family:"Oswald",Arial,sans-serif;font-weight:600;color:var(--green);
  font-size:30px;line-height:1.05;letter-spacing:2px;text-transform:uppercase}
.photo-band{position:absolute;left:0;top:145px;width:878px;height:263px;display:flex;gap:4px;background:var(--white)}
.photo{flex:1}
.photo--garden{background:linear-gradient(160deg,#9cc4e6 0%,#5f9b3c 45%,#c9364b 70%,#3f6e2a 100%)}
.photo--fountain{background:linear-gradient(180deg,#7fa8c9 0%,#c7d6e0 40%,#8a8f86 70%,#4f6b3a 100%)}
.photo--wall{background:linear-gradient(200deg,#a7c3d8 0%,#7a8f5c 40%,#a68a6a 70%,#6c5a46 100%)}
.phone-tag{position:absolute;left:344px;top:420px;width:190px;height:42px;background:var(--white);
  border-radius:21px;display:flex;align-items:center;justify-content:center;gap:10px;
  font-family:"Oswald",Arial,sans-serif;font-weight:500;font-size:23px;color:var(--ink)}
.phone-tag svg{width:23px;height:23px}
.content{position:absolute;left:30px;top:476px;width:818px;height:568px;background:var(--cream);padding:18px 28px}
.columns{display:flex;gap:34px}
.service{flex:1}
.content h2{font-family:"Oswald",Arial,sans-serif;font-weight:600;color:var(--green);
  font-size:20px;text-transform:uppercase;margin-bottom:6px;letter-spacing:.5px;line-height:1.2}
.content p{font-size:11px;line-height:1.5;margin-bottom:7px}
.turf{margin-top:6px}
.turf h2{text-align:center}
.turf-body{display:flex;gap:30px;align-items:flex-start}
.turf-intro{flex:1}
.price-list{flex:1;border-collapse:collapse;font-size:11px}
.price-list th{font-family:"Oswald",Arial,sans-serif;font-weight:500;font-size:12px;color:var(--white);
  background:var(--green);text-align:left;padding:4px 8px;letter-spacing:.5px}
.price-list th.price,.price-list td.price{text-align:right}
.price-list td{padding:4px 8px;border-bottom:1px solid var(--rule)}
.price-list td.price{font-weight:700;color:var(--green-dark)}
.price-note{font-size:10px;font-style:normal;color:#6a6a6a;margin-top:4px}
.partners{display:flex;justify-content:space-around;align-items:center;margin-top:14px}
.partner{height:42px;border-radius:6px}
.partner--a{width:110px;background:#2f5c8f}
.partner--b{width:74px;background:#e0ddd2}
.partner--c{width:110px;background:#6aa84f}
.partner--d{width:100px;background:#9ac33c}
.contact-bar{position:absolute;left:0;top:1060px;width:878px;height:140px;background:var(--white);
  border-top:6px solid var(--green);display:flex;justify-content:space-around;align-items:center;
  font-size:12px;color:var(--ink)}
.contact-item{display:flex;align-items:center;gap:8px;line-height:1.5}
.contact-item svg{width:18px;height:18px;flex:none}
</style>
</head>
<body>
<div class="brochure">
  <header class="masthead">
    <div class="brand-dot"></div>
    <div class="brand-name">Brinvale<br>Landworks Group</div>
  </header>

  <section class="photo-band">
    <div class="photo photo--garden" role="img" aria-label="Landscaped garden with red flower beds and lawn"></div>
    <div class="photo photo--fountain" role="img" aria-label="Stone water feature and fountains"></div>
    <div class="photo photo--wall" role="img" aria-label="Worker building a stone retaining wall"></div>
  </section>

  <div class="phone-tag">
    <svg viewBox="0 0 24 24"><circle cx="12" cy="12" r="12" fill="#3d8b2f"/><path d="M8.5 6.5l2 2.5-1.2 1.5c.8 1.7 2.2 3.1 3.9 3.9l1.5-1.2 2.5 2-1.2 2c-4.8-.3-8.7-4.2-9-9z" fill="#fff"/></svg>
    <span>519 555 0192</span>
  </div>

  <main class="content">
    <div class="columns">
      <section class="service">
        <h2>Landscape Construction</h2>
        <p>From outdoor kitchens to water features and garden beds, we design and build outdoor spaces made for living. For over 20 years our crews have brought craftsmanship and care to every stone, plant and fixture we place.</p>
        <p>Whether you picture a patio kitchen for summer evenings or a quiet pond with a gentle waterfall, our team will guide you from first sketch to final walkthrough, on time and on budget.</p>
      </section>
      <section class="service">
        <h2>Property Maintenance</h2>
        <p>Keep your home or commercial property looking its best all season long. Our maintenance crews handle weekly lawn mowing, trimming, edging and cleanup so your grounds always make a great first impression.</p>
        <p>We also care for your gardens with seasonal planting, weeding, pruning and mulching. Ask about our spring and fall cleanup packages for high end residential and commercial clients.</p>
      </section>
    </div>

    <section class="turf">
      <h2>Turf Care</h2>
      <div class="turf-body">
        <div class="turf-intro">
          <p>A healthy lawn starts below the surface. Our turf care program feeds, opens and thickens your grass through the season for a deep green, weed resistant lawn.</p>
          <p>Every visit is carried out by trained technicians using quality products suited to local soil and climate. Combine services for savings across the season.</p>
        </div>
        <div>
          <table class="price-list">
            <thead>
              <tr><th>Service</th><th class="price">From</th></tr>
            </thead>
            <tbody>
              <tr><td>Fertilizer application (per visit)</td><td class="price">$55</td></tr>
              <tr><td>Core aeration</td><td class="price">$95</td></tr>
              <tr><td>Over seeding</td><td class="price">$120</td></tr>
              <tr><td>Full season program (5 visits)</td><td class="price">$349</td></tr>
            </tbody>
          </table>
          <p class="price-note">Prices based on lawns up to 5,000 sq ft.</p>
        </div>
      </div>
    </section>

    <div class="partners">
      <div class="partner partner--a"></div>
      <div class="partner partner--b"></div>
      <div class="partner partner--c"></div>
      <div class="partner partner--d"></div>
    </div>
  </main>

  <footer class="contact-bar">
    <div class="contact-item">
      <svg viewBox="0 0 24 24"><path d="M12 2a7 7 0 0 0-7 7c0 5 7 13 7 13s7-8 7-13a7 7 0 0 0-7-7zm0 9.5A2.5 2.5 0 1 1 12 6.5a2.5 2.5 0 0 1 0 5z" fill="#3d8b2f"/></svg>
      <span>14 Harrow Lane, Elmira,<br>Ontario N0B 1K0</span>
    </div>
    <div class="contact-item">
      <svg viewBox="0 0 24 24"><path d="M6.5 3l3 3.5-1.6 2c1.1 2.4 3 4.3 5.4 5.4l2-1.6 3.5 3-1.6 3C10.8 17.9 6.1 13.2 5.7 6z" fill="#3d8b2f"/></svg>
      <span>t 519 555 0192<br>f 519 555 0147</span>
    </div>
    <div class="contact-item">
      <svg viewBox="0 0 24 24"><rect x="2" y="5" width="20" height="14" rx="2" fill="#3d8b2f"/><path d="M3 6l9 7 9-7" stroke="#fff" stroke-width="1.6" fill="none"/></svg>
      <span>dorrel@brinvalelandworks.com<br>www.brinvalelandworks.com</span>
    </div>
  </footer>
</div>
</body>
</html>
```